Website design for a construction company

The logo and the copies of all the 3 pages are attached below. I don't have a preference in colors but I would ideally like to use the colors on my logo, dark teal (secondary) and copper (primary).

Company Name: Corvel Group

Location: London, UK

Business Overview:

Corvel Group is a comprehensive construction company based in London, specializing in a wide range of construction services. We cater to various sectors, providing services including electrical work, painting and decorating, plastering, plumbing, carpentry, kitchen and bathroom installations, loft conversions, and extensions. Our team is known for its skilled craftsmanship, attention to detail, and commitment to quality.

What "CORVEL" stands for:

Our company name, 'CORVEL', is derived from Corvelion, the ancient Greek god of craftsmen, blacksmiths, artisans, sculptors, metals, metallurgy, fire, and volcanoes. Corvelion was renowned in mythology for his incredible skill in crafting and creating, making him the patron of all craftsmen and artisans. His name is synonymous with the mastery of artisanship and the creation of wondrous, enduring works.

In choosing 'CORVEL' as our name, we embody the spirit and skills of Corvelion. It reflects our commitment to craftsmanship, excellence, and durability in the field of construction. Just as Corvelion was known for his meticulous work, precision, and innovative creations, our company strives to uphold these qualities in every project we undertake.

Our name is a constant reminder of our dedication to quality, innovation, and the art of building. It symbolizes our endeavor to achieve the highest standards in construction, much like Corvelion did in his timeless creations. In essence, 'CORVEL' is not just our name; it's a representation of our ethos and the high standards we set for ourselves in the construction industry.

Target Audience:

Our primary audience includes homeowners, real estate developers, and commercial clients in London seeking reliable, high-quality construction services.

Unique Selling Points:

Diverse Range of Services: Offering a one-stop solution for all construction needs.

Certified and Experienced: Professional team with a strong focus on delivering certified and compliant work, particularly in electrical services.

Client-Centric Approach: Emphasizing client satisfaction, we tailor our services to meet the unique needs and visions of our clients.

Quality and Reliability: Commitment to high-quality materials, skilled workmanship, and delivering projects on time and within budget.

Website Requirements:

Clean, professional design reflecting the quality and reliability of our services.

User-friendly navigation to easily access information about our services, portfolio, company background, and contact details.

Portfolio section showcasing our past projects with placeholders for images and descriptions.

Integration of a contact form, map for our location, and links to our social media accounts.

Mobile-responsive design to ensure accessibility across various devices.

Purpose of the Website:
The website aims to:

Establish an online presence and credibility in the construction industry.

Provide an informative resource about our services and past projects to potential clients.

Facilitate easy communication and inquiries through an integrated contact system.

Tone and Style:

Professional, informative, and welcoming. The website should convey trustworthiness and expertise in the construction field.

Target Market(s)

homeowners, real estate developers, and commercial clients

Industry/Entity Type

Construction

Number of Pages Required

3 page

Colors

Designer to choose colors to be used in the design.

```html
<!DOCTYPE html>
<html lang="en">
<head>
<meta charset="UTF-8">
<title>Corvel Group – Construction in London</title>
<link href="https://fonts.googleapis.com/css2?family=Oswald:wght@400;500;600&family=Poppins:wght@300;400;500;600&display=swap" rel="stylesheet">
<style>
:root{
  --teal:#17807c;
  --teal-dark:#0f5e5b;
  --copper:#c99a3a;
  --copper-dark:#a87a24;
  --ink:#1c2630;
  --text:#4d5660;
  --light:#f4f6f6;
  --white:#ffffff;
  --footer:#121417;
}
*{margin:0;padding:0;box-sizing:border-box}
html,body{width:1200px;height:3560px;overflow:hidden}
body{position:relative;background:var(--white);font-family:"Poppins",Arial,sans-serif;color:var(--text);font-size:13px;line-height:1.6}
.abs{position:absolute}
h1,h2,h3{font-family:"Oswald",Arial,sans-serif;font-weight:500;color:var(--ink);letter-spacing:1px}
.btn{display:inline-block;background:var(--teal);color:var(--white);font-size:12px;font-weight:500;padding:9px 22px;border-radius:3px;text-decoration:none;white-space:nowrap}
.btn-copper{background:var(--copper)}

/* header */
.site-header{left:0;top:0;width:1200px;height:48px;background:rgba(255,255,255,.96);display:flex;align-items:center;padding:0 60px;z-index:5;white-space:nowrap}
.brand{display:flex;align-items:center;gap:8px;font-family:"Oswald",sans-serif;font-weight:600;font-size:18px;color:var(--teal);letter-spacing:1px;white-space:nowrap}
.brand-mark{width:18px;height:18px;background:var(--teal)}
.main-nav{display:flex;gap:20px;margin-left:110px;font-size:12px}
.main-nav a{color:var(--ink);text-decoration:none;white-space:nowrap}
.main-nav a.active{color:var(--teal);font-weight:600}
.header-contact{display:flex;align-items:center;gap:16px;margin-left:auto;font-size:12px;color:var(--ink)}
.header-contact span{display:flex;align-items:center;gap:6px;white-space:nowrap}

/* hero */
.hero-photo{left:0;top:0;width:1200px;height:620px;background:linear-gradient(180deg,#cfdbe3 0%,#b8c6cf 30%,#9c8b73 55%,#7b6550 78%,#5c4a3b 100%)}
.hero-copy{left:0;top:84px;width:1200px;text-align:center}
.hero-title{display:flex;align-items:center;justify-content:center;gap:22px;font-size:44px;font-weight:600;color:var(--ink)}
.hero-title::before,.hero-title::after{content:"";width:70px;height:3px;background:var(--teal)}
.hero-sub{margin-top:10px;font-size:17px;color:var(--ink);line-height:1.5}
.hero-copy .btn{margin-top:18px}

/* about */
.about-photo{left:120px;top:700px;width:380px;height:420px;background:linear-gradient(135deg,#c4873e 0%,#d7c3a6 45%,#5d8d8a 100%)}
.section-heading{display:flex;align-items:center;gap:18px;font-size:36px;white-space:nowrap}
.section-heading.center{justify-content:center}
.section-heading.center::before,.section-heading::after{content:"";width:70px;height:2px;background:var(--teal)}
.section-heading.left::before{content:"";width:70px;height:2px;background:var(--teal)}
.section-heading.left::after{display:none}
.about-copy{left:560px;top:860px;width:520px}
.about-copy p{margin:18px 0 22px;font-size:13px}

.watermark{left:0;width:1200px;text-align:center;font-family:"Oswald",sans-serif;font-weight:600;font-size:120px;letter-spacing:22px;color:rgba(23,128,124,.05);line-height:1;white-space:nowrap;z-index:0}
.watermark.on-dark{color:rgba(255,255,255,.05)}

/* services */
.services-head{left:0;top:1160px;width:1200px;text-align:center}
.services-head p{width:600px;margin:10px auto 0;font-size:13px}
.service-grid{left:112px;top:1262px;width:972px;display:grid;grid-template-columns:repeat(4,228px);column-gap:20px;row-gap:28px;z-index:1}
.service-photo{height:222px;background:linear-gradient(160deg,#b58756,#6d584a)}
.service-card:nth-child(2) .service-photo{background:linear-gradient(160deg,#d9d3c6,#8d7d6a)}
.service-card:nth-child(3) .service-photo{background:linear-gradient(160deg,#c88b5a,#e3d4bf)}
.service-card:nth-child(4) .service-photo{background:linear-gradient(160deg,#a8afb3,#6d7880)}
.service-card:nth-child(5) .service-photo{background:linear-gradient(160deg,#d6b07c,#9a6d41)}
.service-card:nth-child(6) .service-photo{background:linear-gradient(160deg,#e2ddd4,#a09582)}
.service-card:nth-child(7) .service-photo{background:linear-gradient(160deg,#c9b49a,#7e6c5b)}
.service-card:nth-child(8) .service-photo{background:linear-gradient(160deg,#9fb1bd,#5e6a72)}
.service-label{display:flex;gap:8px;margin-top:10px}
.service-icon{flex:0 0 22px;height:22px;border-radius:50%;background:var(--copper)}
.service-label h3{font-size:13px;letter-spacing:.5px;line-height:1.3}
.service-label p{font-size:10px;line-height:1.45;margin-top:2px}
.services-cta{left:0;top:1900px;width:1200px;text-align:center;z-index:1}

/* why choose */
.why-band{left:0;top:2040px;width:1200px;height:530px;background:linear-gradient(120deg,var(--teal) 0%,var(--teal-dark) 100%)}
.why-photo{left:112px;top:2140px;width:488px;height:430px;background:linear-gradient(150deg,#9fc0d6 0%,#d7dfe4 40%,#c99a3a 75%,#7b5c35 100%)}
.why-copy{left:636px;top:2150px;width:460px;color:#e8f1f0}
.why-copy .section-heading{color:var(--white);font-size:34px}
.why-copy .section-heading::before{background:var(--copper)}
.why-copy h4{font-family:"Poppins",sans-serif;font-size:14px;font-weight:600;color:var(--copper);margin-top:16px}
.why-copy p{font-size:11px;line-height:1.55;margin-top:4px}
.why-copy .btn{margin-top:18px}

/* testimonial */
.testimonial-head{left:0;top:2680px;width:1200px}
.avatar{left:560px;top:2756px;width:80px;height:80px;border-radius:50%;background:linear-gradient(160deg,#d8c2a8,#6f5747)}
.quote{left:300px;top:2860px;width:600px;text-align:center;font-size:12px;color:var(--text)}
.quote cite{display:block;margin-top:6px;font-style:normal;font-size:11px;color:var(--ink)}
.arrow{top:2840px;width:36px;height:36px;border-radius:50%;border:1px solid #9aa3a8;background:var(--white)}
.arrow svg{width:34px;height:34px}

/* cta */
.cta-box{left:140px;top:3060px;width:948px;height:228px;border-radius:20px 20px 0 0;background:linear-gradient(100deg,var(--teal) 0%,#3d8a6f 55%,var(--copper) 100%);text-align:center;padding-top:46px;z-index:2}
.cta-box p{font-family:"Poppins",sans-serif;font-size:25px;font-weight:500;color:var(--white);line-height:1.4;width:780px;margin:0 auto}
.cta-box .btn{margin-top:22px;background:var(--white);color:var(--teal)}

/* footer */
.site-footer{left:0;top:3288px;width:1200px;height:272px;background:var(--footer);color:#c6cbce;font-size:11px}
.footer-cols{position:absolute;left:112px;top:36px;display:flex}
.footer-col{width:250px;padding-right:24px}
.footer-col:first-child{width:300px;padding-right:40px}
.footer-col h5{font-family:"Oswald",sans-serif;font-weight:500;font-size:20px;color:var(--white);letter-spacing:1px;margin-bottom:10px}
.footer-col ul{list-style:none}
.footer-col li{margin-bottom:5px;display:flex;align-items:flex-start;gap:8px}
.footer-col .brand{color:var(--white);font-size:22px;margin-bottom:12px}
.footer-col .brand-mark{background:var(--copper)}
.dot{flex:0 0 12px;height:12px;border-radius:50%;background:var(--copper);margin-top:2px}
.copyright{position:absolute;left:0;bottom:0;width:1200px;height:32px;border-top:1px solid #2a2e33;text-align:center;line-height:32px;font-size:10px;color:#8a9095}
</style>
</head>
<body>

<header class="site-header abs">
  <div class="brand"><span class="brand-mark"></span>CORVEL GROUP</div>
  <nav class="main-nav">
    <a class="active" href="#">Home</a><a href="#">About Us</a><a href="#">Solutions</a><a href="#">Projects</a><a href="#">Services</a><a href="#">Blog</a>
  </nav>
  <div class="header-contact">
    <span><svg width="12" height="12" viewBox="0 0 24 24"><path fill="#17807c" d="M6.6 10.8a15 15 0 0 0 6.6 6.6l2.2-2.2a1 1 0 0 1 1-.25 11.4 11.4 0 0 0 3.6.57 1 1 0 0 1 1 1V20a1 1 0 0 1-1 1A17 17 0 0 1 3 4a1 1 0 0 1 1-1h3.5a1 1 0 0 1 1 1c0 1.25.2 2.45.57 3.57a1 1 0 0 1-.25 1z"/></svg>020-7946-0381</span>
    <span><svg width="12" height="12" viewBox="0 0 24 24"><path fill="#17807c" d="M2 5h20v14H2zm2 2v.5l8 5 8-5V7l-8 5z"/></svg>info@corvelgroup.com</span>
    <a class="btn" href="#">Contact Now</a>
  </div>
</header>

<section class="hero">
  <div class="hero-photo abs" role="img" aria-label="Construction site with excavators moving earth under a clear sky"></div>
  <div class="hero-copy abs">
    <h1 class="hero-title">BUILDING YOUR DREAMS INTO REALITY</h1>
    <p class="hero-sub">Expert Craftsmanship Meets Unmatched Reliability in the Heart of London<br>Introduction Section</p>
    <a class="btn" href="#">Get Started</a>
  </div>
</section>

<section class="about">
  <div class="about-photo abs" role="img" aria-label="Tall buildings under construction with cranes against the sky"></div>
  <div class="about-copy abs">
    <h2 class="section-heading left">ABOUT US</h2>
    <p>"Welcome to Corvel Group – Where Construction Meets Excellence. Based in London, we are committed to transforming your spaces into exceptional places. Our team is dedicated to delivering the highest quality in every project, attending to every detail with precision and care."</p>
    <a class="btn" href="#">Get Started</a>
  </div>
</section>

<section class="services">
  <div class="watermark abs" style="top:1800px">CORVEL GROUP</div>
  <div class="services-head abs">
    <h2 class="section-heading center">OUR SERVICES</h2>
    <p>Tailored to Your Needs: Discover how we can bring your vision to life, covering every aspect of construction from the initial design to the final touches.</p>
  </div>
  <div class="service-grid abs">
    <article class="service-card"><div class="service-photo" role="img" aria-label="Electrician working on a wiring panel"></div><div class="service-label"><span class="service-icon"></span><div><h3>ELECTRICAL WORK</h3><p>Lorem Ipsum is simply dummy text of the printing and typesetting industry.</p></div></div></article>
    <article class="service-card"><div class="service-photo" role="img" aria-label="Painter rolling paint onto a wall"></div><div class="service-label"><span class="service-icon"></span><div><h3>PAINTING AND DECORATING</h3><p>Lorem Ipsum is simply dummy text of the printing and typesetting industry.</p></div></div></article>
    <article class="service-card"><div class="service-photo" role="img" aria-label="Plasterer smoothing a brick wall"></div><div class="service-label"><span class="service-icon"></span><div><h3>PLASTERING</h3><p>Lorem Ipsum is simply dummy text of the printing and typesetting industry.</p></div></div></article>
    <article class="service-card"><div class="service-photo" role="img" aria-label="Plumber fitting pipes under a sink"></div><div class="service-label"><span class="service-icon"></span><div><h3>PLUMBING</h3><p>Lorem Ipsum is simply dummy text of the printing and typesetting industry.</p></div></div></article>
    <article class="service-card"><div class="service-photo" role="img" aria-label="Carpenter cutting timber in a workshop"></div><div class="service-label"><span class="service-icon"></span><div><h3>CARPENTRY</h3><p>Lorem Ipsum is simply dummy text of the printing and typesetting industry.</p></div></div></article>
    <article class="service-card"><div class="service-photo" role="img" aria-label="Modern kitchen and bathroom installation"></div><div class="service-label"><span class="service-icon"></span><div><h3>KITCHEN AND BATHROOM INSTALLATIONS</h3><p>Lorem Ipsum is simply dummy text of the printing and typesetting.</p></div></div></article>
    <article class="service-card"><div class="service-photo" role="img" aria-label="Converted loft room under a pitched roof"></div><div class="service-label"><span class="service-icon"></span><div><h3>LOFT CONVERSIONS</h3><p>Lorem Ipsum is simply dummy text of the printing and typesetting industry.</p></div></div></article>
    <article class="service-card"><div class="service-photo" role="img" aria-label="House extension under construction"></div><div class="service-label"><span class="service-icon"></span><div><h3>EXTENSIONS</h3><p>Lorem Ipsum is simply dummy text of the printing and typesetting industry.</p></div></div></article>
  </div>
  <div class="services-cta abs"><a class="btn" href="#">View All Services</a></div>
</section>

<section class="why">
  <div class="why-band abs"></div>
  <div class="watermark on-dark abs" style="top:2440px">CORVEL GROUP</div>
  <div class="why-photo abs" role="img" aria-label="Two site engineers in hard hats reviewing plans before a high-rise"></div>
  <div class="why-copy abs">
    <h2 class="section-heading left">WHY CHOOSE US</h2>
    <h4>Our Expertise</h4>
    <p>"Leveraging over 15 years of experience, Corvel Group stands as a beacon of excellence in the construction industry. We handle projects of every size with skill, care and precision."</p>
    <h4>Quality Assurance</h4>
    <p>"Quality is not just a promise but a guarantee. We use only trusted materials and proven methods, so every finished space stands strong for years to come."</p>
    <h4>Certified Excellence</h4>
    <p>"Your safety and satisfaction are our top priorities. Our certified team works to the highest industry standards, delivering compliant work you can rely on."</p>
    <a class="btn btn-copper" href="#">Learn More</a>
  </div>
</section>

<section class="testimonial">
  <div class="testimonial-head abs"><h2 class="section-heading center">OUR TESTIMONIAL</h2></div>
  <div class="avatar abs" role="img" aria-label="Portrait of a satisfied client"></div>
  <div class="arrow abs" style="left:70px"><svg viewBox="0 0 34 34"><path d="M19 11l-6 6 6 6" fill="none" stroke="#1c2630" stroke-width="2"/></svg></div>
  <div class="arrow abs" style="left:1094px"><svg viewBox="0 0 34 34"><path d="M15 11l6 6-6 6" fill="none" stroke="#1c2630" stroke-width="2"/></svg></div>
  <blockquote class="quote abs">"Hear from Our Satisfied Clients: Our commitment to excellence has earned us the trust of numerous homeowners and businesses in London. Read their stories and understand the Corvel Group difference."<cite>– Laura Denholm</cite></blockquote>
</section>

<section class="cta-box abs">
  <p>"Ready to Start Your Project? Contact us today for a consultation and embark on the journey to turn your construction dreams into a stunning reality."</p>
  <a class="btn" href="#">Get Started</a>
</section>

<footer class="site-footer abs">
  <div class="footer-cols">
    <div class="footer-col">
      <div class="brand"><span class="brand-mark"></span>CORVEL GROUP</div>
      <p>Lorem Ipsum is simply dummy text of the printing and typesetting industry. Lorem Ipsum has been the industry's standard dummy text ever since the 1500s.</p>
    </div>
    <div class="footer-col">
      <h5>QUICK LINKS</h5>
      <ul><li>Home</li><li>About Us</li><li>Services</li><li>Contact Us</li></ul>
    </div>
    <div class="footer-col">
      <h5>CONTACT US</h5>
      <ul><li><span class="dot"></span>020-7946-0381</li><li><span class="dot"></span>Lorem Ipsum is simply dummy text of the printing.</li><li><span class="dot"></span>info@corvelgroup.com</li></ul>
    </div>
    <div class="footer-col">
      <h5>FOLLOW US</h5>
      <ul><li><span class="dot"></span>Friendsphere</li><li><span class="dot"></span>Snapgrid</li><li><span class="dot"></span>Chirper</li><li><span class="dot"></span>Linkwork</li></ul>
    </div>
  </div>
  <div class="copyright">Copyright © 2024 Corvel Group – All Rights Reserved</div>
</footer>

</body>
</html>
```